Velmora Ridge Tours Brochure Design

We are a start up Tour Operator company specialising in Tours to Africa - specifically South Africa, Zimbabwe, Zambia, Ethiopia, Botswana, Tanzania, Kenya.
We need to create a brochure that details a number of our tours categorised by country. We ideally want it to be square or A4/A5. We do not want it to be too think.
We want to use a variety of images from the locations, which I can provide.
It needs to be high quality.
We want our logo incorporated into the brochure - particularly on the first page.
Industry/Entity Type
Travel Agent
Requirements
Must have
- Our logo
- Photos
- Tour summaries with prices (as per documents uploaded)
- Brochure should be broken down into:
- About Us
- Section for Each Country
- Multi-Country Tours
- Tailormade Tours
- Needs to be in a format that I can then alter afterwards as we add in more tours etc
Nice to have
- RGB 170, 170, 117 is a company colour scheme - ideally will be the base background colour. However, not firm on this.

```html
<!DOCTYPE html>
<html lang="en">
<head>
<meta charset="utf-8">
<title>Velmora Ridge Tours – Brochure</title>
<link href="https://fonts.googleapis.com/css2?family=Chicle&family=Ranchers&family=Open+Sans:wght@400&display=swap" rel="stylesheet">
<style>
  :root {
    --stage: #e4e4e4;
    --ink: #141414;
    --ink-soft: #23261f;
    --paper-text: #f3efe6;
    --sunset-hot: #f39a1c;
    --sunset-red: #c2410c;
    --sunset-deep: #5a1d06;
    --heading-a: #f7a21b;
    --heading-b: #d3331a;
    --pattern-orange: #e26a1f;
    --pattern-red: #a3261b;
    --savanna-green: #6a9a3a;
    --sky-blue: #7fb2d9;
  }
  * { box-sizing: border-box; margin: 0; padding: 0; }
  html, body { width: 1200px; height: 982px; overflow: hidden; }
  body { background: var(--stage); position: relative; font-family: "Ranchers", "Arial Black", sans-serif; color: var(--paper-text); }

  .brochure {
    position: absolute; left: 60px; top: 111px; width: 1080px; height: 760px;
    background: var(--ink); box-shadow: 0 8px 24px rgba(0,0,0,.25);
    overflow: hidden;
  }
  .panel { position: absolute; top: 0; width: 360px; height: 760px; }
  .panel--inside-left { left: 0; }
  .panel--inside-middle { left: 360px; border-left: 1px solid rgba(255,255,255,.05); }
  .panel--cover { left: 720px; background: linear-gradient(180deg, var(--ink) 0%, var(--ink-soft) 100%); }

  .scene-sunset {
    position: absolute; left: 0; top: 0; width: 720px; height: 250px;
    background: linear-gradient(180deg, var(--sunset-red) 0%, var(--sunset-hot) 45%, var(--sunset-deep) 75%, var(--ink) 100%);
  }
  .scene-savanna {
    position: absolute; left: 0; bottom: 0; width: 720px; height: 280px;
    background:
      radial-gradient(ellipse at 42% 80%, rgba(122,170,40,.55) 0%, transparent 40%),
      linear-gradient(180deg, var(--ink) 0%, var(--sunset-deep) 50%, var(--sunset-red) 85%, #3a1204 100%);
  }

  .photo { position: absolute; border: 2px solid var(--paper-text); }
  .photo--dawn { background: linear-gradient(180deg, #f2c27a, #b8692a); }
  .photo--plains { background: linear-gradient(180deg, var(--sky-blue), var(--savanna-green)); }
  .photo--dusk { background: linear-gradient(180deg, #f4a23a, #3b1a08); }

  .tours-title {
    position: absolute; left: 150px; top: 42px;
    font-family: "Chicle", "Impact", sans-serif; font-size: 40px; letter-spacing: 2px;
    color: var(--heading-b);
  }
  .tours-photo { left: 40px; top: 110px; width: 240px; height: 160px;
    background: linear-gradient(180deg, var(--sky-blue) 0%, #8c7f6a 60%, var(--pattern-orange) 100%); }
  .tours-countries { position: absolute; left: 120px; top: 285px; width: 210px; font-size: 13px; line-height: 1.25; }

  .body-copy { position: absolute; font-size: 10px; line-height: 1.35; letter-spacing: .3px; }
  .body-copy--left { left: 40px; top: 360px; width: 290px; }
  .body-copy--mid-top { left: 70px; top: 150px; width: 260px; }
  .body-copy--mid-bottom { left: 40px; top: 470px; width: 280px; }

  .footer-line { position: absolute; left: 30px; bottom: 18px; width: 670px; font-size: 11px; letter-spacing: .5px; }

  .grid-a1 { left: 30px; top: 280px; width: 90px; height: 60px; }
  .grid-a2 { left: 130px; top: 290px; width: 95px; height: 64px; }
  .grid-a3 { left: 240px; top: 300px; width: 95px; height: 64px; }
  .grid-b1 { left: 30px; top: 355px; width: 90px; height: 60px; }
  .grid-b2 { left: 130px; top: 370px; width: 95px; height: 64px; }
  .grid-b3 { left: 240px; top: 380px; width: 95px; height: 64px; }
  .strip-1 { left: 30px; top: 600px; width: 85px; height: 60px; }
  .strip-2 { left: 125px; top: 590px; width: 120px; height: 80px; }
  .strip-3 { left: 255px; top: 605px; width: 85px; height: 60px; }

  .brand { position: absolute; left: 70px; top: 60px; display: flex; align-items: center; gap: 12px; }
  .brand__mark { width: 46px; height: 46px; border-radius: 50%; background: var(--heading-b); }
  .brand__name { font-size: 22px; line-height: 1.05; color: var(--paper-text); width: 170px; }

  .lion-frame { position: absolute; left: 30px; top: 170px; width: 300px; height: 300px;
    background: linear-gradient(135deg, var(--pattern-red), var(--pattern-orange)); }
  .lion-photo { position: absolute; left: 14px; top: 14px; width: 272px; height: 272px;
    background: radial-gradient(circle at 50% 45%, #d9a765 0%, #b77a3d 55%, #6e4420 100%); }
  .lion-caption { position: absolute; left: 40px; top: 400px; width: 220px;
    font-family: "Open Sans", Arial, sans-serif; font-size: 15px; line-height: 1.2; color: var(--paper-text); }

  .cover-headline { position: absolute; left: 30px; top: 495px; width: 300px; font-size: 20px; line-height: 1.2; letter-spacing: 1px; }

  .pattern-band { position: absolute; left: 0; bottom: 0; width: 360px; height: 120px;
    background: linear-gradient(180deg, var(--pattern-orange), var(--pattern-red)); }
</style>
</head>
<body>
  <main class="brochure">
    <div class="scene-sunset" role="img" aria-label="Sunset sky with silhouetted elephants and acacia tree"></div>
    <div class="scene-savanna" role="img" aria-label="Savanna sunset with giraffe and acacia silhouettes"></div>

    <section class="panel panel--inside-left">
      <h2 class="tours-title">OUR TOURS</h2>
      <div class="photo tours-photo" role="img" aria-label="Mountain landscape with a map of Africa overlay"></div>
      <p class="tours-countries">SOUTH-AFRICA, ZIMBABWE, ZAMBIA, ETHIOPIA, BOTSWANA, TANZANIA, KENYA.</p>
      <p class="body-copy body-copy--left">LOREM IPSUM DOLOR SIT AMET, CONSECTETUR ADIPISCING ELIT, SED DO EIUSMOD TEMPOR INCIDIDUNT UT LABORE ET DOLORE MAGNA ALIQUA. UT ENIM AD MINIM VENIAM, QUIS NOSTRUD EXERCITATION ULLAMCO LABORIS NISI UT ALIQUIP EX EA COMMODO CONSEQUAT. DUIS AUTE IRURE DOLOR IN REPREHENDERIT IN VOLUPTATE VELIT ESSE CILLUM DOLORE EU FUGIAT NULLA PARIATUR.</p>
    </section>

    <section class="panel panel--inside-middle">
      <p class="body-copy body-copy--mid-top">LOREM IPSUM DOLOR SIT AMET, CONSECTETUR ADIPISCING ELIT, SED DO EIUSMOD TEMPOR INCIDIDUNT UT LABORE ET DOLORE MAGNA ALIQUA. UT ENIM AD MINIM VENIAM, QUIS NOSTRUD EXERCITATION ULLAMCO LABORIS NISI UT ALIQUIP EX EA COMMODO CONSEQUAT. DUIS AUTE IRURE DOLOR IN REPREHENDERIT IN VOLUPTATE VELIT ESSE CILLUM DOLORE EU FUGIAT NULLA PARIATUR.</p>
      <div class="photo photo--dawn grid-a1" role="img" aria-label="Safari vehicle at dawn"></div>
      <div class="photo photo--plains grid-a2" role="img" aria-label="Herd on green plains"></div>
      <div class="photo photo--dusk grid-a3" role="img" aria-label="Acacia tree at dusk"></div>
      <div class="photo photo--dawn grid-b1" role="img" aria-label="Lake at sunrise"></div>
      <div class="photo photo--dusk grid-b2" role="img" aria-label="Elephants under an acacia at sunset"></div>
      <div class="photo photo--plains grid-b3" role="img" aria-label="Waterhole under blue sky"></div>
      <p class="body-copy body-copy--mid-bottom">LOREM IPSUM DOLOR SIT AMET, CONSECTETUR ADIPISCING ELIT, SED DO EIUSMOD TEMPOR INCIDIDUNT UT LABORE ET DOLORE MAGNA ALIQUA. UT ENIM AD MINIM VENIAM, QUIS NOSTRUD EXERCITATION ULLAMCO LABORIS NISI UT ALIQUIP EX EA COMMODO CONSEQUAT. DUIS AUTE IRURE DOLOR IN REPREHENDERIT IN VOLUPTATE VELIT ESSE CILLUM DOLORE EU FUGIAT NULLA PARIATUR.</p>
      <div class="photo photo--dawn strip-1" role="img" aria-label="Cloudy savanna horizon"></div>
      <div class="photo photo--dusk strip-2" role="img" aria-label="Elephants beneath an acacia at sunset"></div>
      <div class="photo photo--dawn strip-3" role="img" aria-label="Sunset over the plains"></div>
    </section>

    <p class="footer-line">LOREM IPSUM DOLOR SIT AMET, CONSECTETUR ADIPISCING ELIT, SED DO EIUSMOD TEMPOR INCIDIDUNT UT LABORE ET DOLORE</p>

    <section class="panel panel--cover">
      <div class="brand">
        <span class="brand__mark"></span>
        <span class="brand__name">VELMORA RIDGE TOURS</span>
      </div>
      <div class="lion-frame" role="img" aria-label="Decorative African pattern frame">
        <div class="lion-photo" role="img" aria-label="Close-up photograph of a lion"></div>
      </div>
      <p class="lion-caption">Your short and sweet caption goes here</p>
      <h1 class="cover-headline">LOREM IPSUM DOLOR SIT AMET, CONSECTETUR ADIPISICING ELIT, SED DO EIUSMOD TEMPOR INCIDIDUNT</h1>
      <div class="pattern-band" role="img" aria-label="Decorative African pattern band"></div>
    </section>
  </main>
</body>
</html>
```